Healthcare website - Diabetic Shoes - Elderfund - No Cost

I am looking to upgrade my website. I do not want to use Wordpress, Adobe Muse or another designing program. The code should be easily editable using textpad or VI. After the project is done I want to easily add my custom PHP code.

Features
Creative and Modern Design .
Fully responsive site for use on mobile devices
bootstrap, jquery

My current website is
www.pebblewalkco.com

Target Market(s)

Older people who have diabetes. Target market is +60 years old, but we do have younger people going to the site to help out their parents.

Industry/Entity Type

Healthcare

Coding

Coded - Design and coding required

Number of Pages Required

2 page

Colors

Designer to choose colors to be used in the design.

Requirements
Must have
• The code should be easily editable using textpad or VI. After the project is done I want to easily add my custom PHP code.
• The first page will be the home page and the other page I need is this form.
• https://www.pebblewalkco.com/pebble-walk-co-do-i-qualify.php
Should not have
• I do not want to use Wordpress, Adobe Muse or another designing program.

```html
<!DOCTYPE html>
<html lang="en">
<head>
<meta charset="utf-8">
<title>Pebble Walk Co – Do I Qualify?</title>
<link rel="stylesheet" href="https://fonts.googleapis.com/css2?family=Roboto:wght@400;500;700&display=swap">
<style>
:root{
  --green:#6cc461;
  --blue:#4a7ca3;
  --heading:#4b7aa0;
  --brand:#1f8a9c;
  --phone:#2b6fb0;
  --text:#7a7a7a;
  --field-text:#6a6a6a;
  --panel:#ededed;
  --white:#ffffff;
  --footer:#2a76b8;
  --footer-dark:#1b1b1b;
  --orange:#f7941d;
  --check:#d8d8d8;
}
*{box-sizing:border-box;margin:0;padding:0}
html,body{width:1200px;height:2400px;overflow:hidden}
body{position:relative;background:var(--white);font-family:"Roboto",Arial,sans-serif;color:var(--text)}
.abs{position:absolute}

/* header */
.brand{left:128px;top:12px;display:flex;align-items:center;gap:10px;font-size:32px;font-weight:500;color:var(--brand);letter-spacing:.5px}
.brand-dot{width:22px;height:22px;border-radius:50%;background:var(--green)}
.phone{left:790px;top:16px;display:flex;align-items:center;gap:6px;font-size:24px;font-weight:700;color:var(--phone)}
.phone-icon{width:24px;height:24px;border-radius:50%;background:var(--green);display:flex;align-items:center;justify-content:center}
.header-social{top:19px;width:22px;height:22px;background:var(--phone);border-radius:3px}

.nav{left:0;top:66px;width:1200px;height:51px;background:var(--green)}
.nav a{position:absolute;top:0;height:51px;line-height:51px;color:var(--white);font-size:12.5px;font-weight:500;text-decoration:none;white-space:nowrap}
.nav .active{background:var(--blue);left:202px;width:217px;text-align:center}
.nav .login{top:14px;height:23px;line-height:23px;left:962px;width:80px;border-radius:12px;background:var(--blue);text-align:center}

/* intro */
.intro{left:128px;top:150px;width:885px}
.page-title{font-size:38px;font-weight:700;color:var(--heading);margin-bottom:16px}
.intro p{font-size:14.5px;line-height:23px;margin-bottom:23px}

/* form */
.form-panel{left:0;top:403px;width:1200px;height:1837px;background:var(--panel)}
.section-title{position:absolute;left:128px;font-size:35px;font-weight:700;color:var(--heading);line-height:45px;white-space:nowrap}
.field{position:absolute;width:416px;height:52px;background:var(--white);border-radius:3px;font-size:13px;color:var(--field-text);padding-left:14px;line-height:52px}
.col-l{left:128px}
.col-r{left:578px}
.field .caret{position:absolute;right:16px;top:22px}

.products{left:128px;top:1781px;width:866px;height:125px;background:var(--white)}
.check{position:absolute;display:flex;align-items:center;gap:8px;font-size:11.5px;color:var(--field-text)}
.check i{width:14px;height:14px;border:1px solid var(--check);background:#f7f7f7;display:block}

.comments{left:128px;top:2000px;width:416px;height:80px;background:var(--white);border-radius:3px;font-size:13px;padding:22px 14px;color:var(--field-text)}
.consent{left:563px;top:1997px;width:505px;font-size:12.5px;line-height:20px;color:var(--text)}
.submit{left:128px;top:2115px;width:350px;height:52px;background:var(--green);color:var(--white);border-radius:3px;font-size:16px;font-weight:700;text-align:center;line-height:52px}

/* footer */
.footer{left:0;top:2240px;width:1200px;height:122px;background:var(--footer)}
.footer-label{position:absolute;top:30px;font-size:15px;font-weight:500;color:var(--white)}
.footer-social{position:absolute;top:64px;width:35px;height:35px;border:2px solid var(--white);border-radius:4px}
.news-input{position:absolute;left:261px;top:59px;width:219px;height:39px;background:var(--white);font-size:13px;color:var(--field-text);padding-left:12px;line-height:39px}
.news-btn{position:absolute;left:480px;top:59px;width:83px;height:39px;background:var(--orange);color:var(--white);font-size:13px;font-weight:500;text-align:center;line-height:39px}
.badge{position:absolute;background:var(--white)}
.news-text{position:absolute;left:771px;top:57px;width:280px;font-size:16px;line-height:21px;color:var(--white)}
.bottom-bar{left:0;top:2362px;width:1200px;height:38px;background:var(--footer-dark);font-size:10.5px;color:var(--white);line-height:38px}
.bottom-bar .links{position:absolute;left:128px}
.bottom-bar .copy{position:absolute;right:128px}
</style>
</head>
<body>

<header>
  <div class="abs brand"><span>Pebble Walk Co</span><span class="brand-dot"></span></div>
  <div class="abs phone">
    <span class="phone-icon"><svg width="14" height="14" viewBox="0 0 24 24"><path fill="#fff" d="M6.6 10.8a15.1 15.1 0 0 0 6.6 6.6l2.2-2.2c.3-.3.7-.4 1-.2 1.1.4 2.3.6 3.6.6.6 0 1 .4 1 1V20c0 .6-.4 1-1 1A17 17 0 0 1 3 4c0-.6.4-1 1-1h3.5c.6 0 1 .4 1 1 0 1.3.2 2.5.6 3.6.1.3 0 .7-.2 1z"/></svg></span>
    1-800-555-0142
  </div>
  <span class="abs header-social" style="left:1018px"></span>
  <span class="abs header-social" style="left:1046px"></span>
</header>

<nav class="abs nav">
  <a style="left:141px">HOME</a>
  <a class="active">PEBBLE WALK CO! DO I QUALIFY!</a>
  <a style="left:432px">WHY DIABETIC SHOES?</a>
  <a style="left:597px">SHOES</a>
  <a style="left:666px">PRODUCTS</a>
  <a style="left:765px">SHOE FITTER JOBS</a>
  <a style="left:914px">FAQ</a>
  <a class="login">LOGIN</a>
</nav>

<section class="abs intro">
  <h1 class="page-title">Pebble Walk Co Do I Qualify?</h1>
  <p>You may be eligible for shoes - at no cost to you! Enter your information in the form below to find out if you qualify for shoe coverage. Elderfund or your insurance provider may cover the cost of one pair of shoes and three pairs of custom or heat molded insoles per calendar year. Find out if you qualify now!</p>
  <p>Besides Elderfund, here is a list of private insurance providers: Silverpath Senior Health, Averly, Crestmark Health,VetCare Plus, Coveridge, Summit Health Plan, Hollis Health, Blue Harbor Shield, Care Forward, Pinnacle, Safe Meadows, Unity Health Care, Triwell,Goodcare. Any many more.</p>
</section>

<main class="abs form-panel"></main>

<h2 class="section-title" style="top:440px">Personal Information</h2>
<div class="field col-l" style="top:510px">First Name</div>
<div class="field col-r" style="top:510px">Last Name</div>
<div class="field col-l" style="top:578px">Address</div>
<div class="field col-r" style="top:578px">City</div>
<div class="field col-l" style="top:646px">State<svg class="caret" width="14" height="8"><path d="M0 0h14L7 8z" fill="#29a3dc"/></svg></div>
<div class="field col-r" style="top:646px">Zip</div>
<div class="field col-l" style="top:714px">Gender<svg class="caret" width="14" height="8"><path d="M0 0h14L7 8z" fill="#29a3dc"/></svg></div>
<div class="field col-r" style="top:714px">Date of Birth</div>
<div class="field col-l" style="top:782px">Email</div>
<div class="field col-r" style="top:782px">Phone</div>

<h2 class="section-title" style="top:862px">Elderfund and Insurance Information</h2>
<div class="field col-l" style="top:925px">Is Elderfund Your Primary Insurance?<svg class="caret" width="14" height="8"><path d="M0 0h14L7 8z" fill="#29a3dc"/></svg></div>
<div class="field col-r" style="top:925px">Elderfund#:</div>

<h2 class="section-title" style="top:996px">Supplementary/Secondary Insurance Information</h2>
<div class="field col-l" style="top:1061px">Name of Insurance Company?</div>
<div class="field col-l" style="top:1128px">Insurance Phone #:</div>
<div class="field col-l" style="top:1195px">Policy Number / Member Id</div>

<h2 class="section-title" style="top:1276px">Primary Physician Information (M.D or D.O only No<br>Podiatrist Please</h2>
<div class="field col-l" style="top:1387px">First Name:</div>
<div class="field col-r" style="top:1387px">Last Name:</div>
<div class="field col-l" style="top:1454px">Address:</div>
<div class="field col-r" style="top:1454px">City:</div>
<div class="field col-l" style="top:1522px">State</div>
<div class="field col-r" style="top:1522px">Zip:</div>
<div class="field col-l" style="top:1589px">Phone:</div>
<div class="field col-r" style="top:1589px">Fax:</div>

<h2 class="section-title" style="top:1670px">Elderfund Covered Products (Check next to each<br>product you want to receive)</h2>
<div class="abs products">
  <label class="check" style="left:16px;top:23px"><i></i>Tens Unit</label>
  <label class="check" style="left:250px;top:23px"><i></i>Seat Lift</label>
  <label class="check" style="left:485px;top:23px"><i></i>Back Brace</label>
  <label class="check" style="left:16px;top:54px"><i></i>Ankle Brace</label>
  <label class="check" style="left:250px;top:54px"><i></i>Knee Brace</label>
  <label class="check" style="left:485px;top:54px"><i></i>Wrist Brace</label>
  <label class="check" style="left:16px;top:84px"><i></i>Compounded Cream</label>
</div>

<h2 class="section-title" style="top:1939px">Confirm &amp; Submit Application</h2>
<div class="abs comments">Additional Comments</div>
<p class="abs consent">By submitting this information, I authorize PebbleWalkCo.com/Harborline Medical Supply Inc., its affiliates, subsidiaries, or parent company to contact me by phone or email. Please be assured that we value and protect your privacy. Remember, there is no purchase necessary to see if you qualify.</p>
<div class="abs submit">Submit Now</div>

<footer class="abs footer">
  <div class="footer-label" style="left:131px">FOLLOW US</div>
  <span class="footer-social" style="left:131px"></span>
  <span class="footer-social" style="left:179px"></span>
  <div class="footer-label" style="left:259px">SING UP FOR NEWSLETTER</div>
  <div class="news-input">Email..</div>
  <div class="news-btn">SIGN UP</div>
  <span class="badge" style="left:616px;top:29px;width:48px;height:64px"></span>
  <span class="badge" style="left:670px;top:66px;width:58px;height:27px"></span>
  <div class="footer-label" style="left:771px;top:30px">LATEST NEWS</div>
  <p class="news-text">Lorem ipsum dolor sit amet, cmassa. Cum sociis natoque tibus</p>
</footer>
<div class="abs bottom-bar">
  <span class="links">TERMS OF USE &nbsp;|&nbsp; PRIVACY POLICY &nbsp;|&nbsp; RETURN/EXCHANGE</span>
  <span class="copy">© 2017 Pebble Walk Co - All Rights Reserved</span>
</div>

</body>
</html>
```